New florist business website design

Number 1 want is an easy to navigate & check out website
Needs to be beautiful and eye catching as well.
This is an online only business (no shop front)
Rustic and blush pinks, neutrals, woods, leaves
Customers need to be able to go onto my website, select something they want to buy but have the option to use a drop down box to change colours of the flowers, or add notes to make changes to the arrangement

Industry/Entity Type

Florist

Coding

Coded - Design and coding required

Number of Pages Required

5+ page

Colors
f9d9e8
fff2ec
fffefc

Requirements
Must have
• Drop down menu to take you to other pages for Arrangements, bouquets, everlasting arrangements, gifts, contact
Be able to purchase and “add to basket”
Checkout page
Nice to have
• Be able to add my own photos once I’ve taken new ones
Should not have
• Tacky images or clip art

```html
<!DOCTYPE html>
<html lang="en">
<head>
<meta charset="utf-8">
<title>Petal &amp; Fern — Florist</title>
<link href="https://fonts.googleapis.com/css2?family=Jost:wght@300;400;500;600&family=Great+Vibes&display=swap" rel="stylesheet">
<style>
:root{
  --blush:#f9d9e8;
  --cream:#fff2ec;
  --paper:#fffefc;
  --rose:#d4707f;
  --rose-soft:#f3c6cf;
  --ink:#2a2226;
  --muted:#6f6468;
  --band:#d37686;
  --dark:#1f1a1c;
}
*{box-sizing:border-box;margin:0;padding:0}
html,body{width:1200px;height:3980px;overflow:hidden}
body{font-family:"Jost",sans-serif;color:var(--ink);background:var(--paper);position:relative}
.abs{position:absolute}
.script{font-family:"Great Vibes",cursive;font-weight:400}
.btn{position:absolute;display:flex;align-items:center;justify-content:center;border-radius:22px;background:var(--rose-soft);color:var(--ink);font-size:14px;font-weight:500;letter-spacing:.5px;text-transform:uppercase}
.ph{position:absolute}
.wash{position:absolute;left:0;top:0;width:1200px;height:3230px;background:linear-gradient(180deg,#fbe6ec 0%,#fdf1f2 18%,#fff6f4 35%,#fbe4ea 55%,#fff3f1 75%,#fbe6ec 100%)}
.nav{position:absolute;top:52px;font-size:14px;font-weight:500}
.logo{position:absolute;left:530px;top:40px;width:140px;text-align:center;font-size:20px;font-weight:500;color:var(--rose)}
.logo-dot{display:inline-block;width:8px;height:8px;border-radius:50%;background:var(--rose);margin-right:6px;vertical-align:middle}
.hero-title{left:120px;top:290px;font-size:30px;font-weight:500;letter-spacing:1px}
.hero-script{left:120px;top:330px;font-size:72px;line-height:1}
.dots{position:absolute;display:flex;gap:8px}
.dots i{width:8px;height:8px;border-radius:50%;background:#c9b6bb}
.dots i.on{background:var(--ink)}
.welcome-bg{left:600px;top:760px;font-size:110px;color:#f6dbe1}
.welcome-title{left:595px;top:850px;font-size:40px;font-weight:500;line-height:1.2}
.body-text{font-size:14px;line-height:1.6;color:var(--muted)}
.kicker{font-size:20px;font-weight:500;text-align:center}
.script-head{font-size:52px;text-align:center;line-height:1}
.product{position:absolute;width:200px;text-align:center;top:1640px}
.product .pic{width:120px;height:200px;margin:0 auto;border-radius:6px}
.product .name{margin-top:40px;font-size:17px}
.product .price{font-size:30px;font-weight:600;margin-top:4px}
.product.active{background:var(--paper);box-shadow:0 10px 30px rgba(200,120,140,.2);border-radius:8px;padding-top:20px;top:1620px;height:420px}
.arrow{position:absolute;top:1830px;width:20px;height:20px}
.post{position:absolute;top:2770px;width:300px}
.post .pic{height:220px;border-radius:14px}
.post .date{position:absolute;right:80px;top:160px;width:58px;height:58px;border-radius:50%;background:var(--rose);color:#fff;font-size:11px;text-align:center;line-height:1.2;padding-top:14px}
.post h4{font-size:24px;font-weight:500;text-align:center;margin-top:34px}
.post p{font-size:13px;line-height:1.55;color:var(--muted);text-align:center;margin-top:8px;padding:0 10px}
.band{left:0;top:3230px;width:1200px;height:190px;background:var(--band)}
.footer{left:0;top:3420px;width:1200px;height:530px;background:var(--cream)}
.col-h{position:absolute;top:3620px;font-size:24px;font-weight:500}
.links{position:absolute;top:3680px;font-size:14px;line-height:1.65}
.copyright{left:0;top:3950px;width:1200px;height:30px;background:var(--dark);color:#fff;font-size:12px;padding:8px 120px}
</style>
</head>
<body>
<div class="wash"></div>

<svg class="abs" style="left:115px;top:52px" width="60" height="20" viewBox="0 0 60 20" fill="none" stroke="#2a2226" stroke-width="2">
  <path d="M2 4h16M2 10h16M2 16h10"/><circle cx="44" cy="9" r="6"/><path d="M48.5 13.5l5 5"/>
</svg>
<div class="nav" style="left:330px">Shop</div>
<div class="nav" style="left:420px">About</div>
<div class="logo"><span class="logo-dot"></span>Petal &amp; Fern</div>
<div class="nav" style="left:718px">Blog</div>
<div class="nav" style="left:808px">Contact</div>
<svg class="abs" style="left:1010px;top:48px" width="90" height="26" viewBox="0 0 90 26" fill="none" stroke="#2a2226" stroke-width="2">
  <circle cx="10" cy="8" r="5"/><path d="M2 22c1-6 15-6 16 0"/>
  <path d="M58 8h22l-2 14H60z"/><path d="M64 8a5 5 0 0 1 10 0"/>
  <circle cx="82" cy="6" r="5" fill="#d4707f" stroke="none"/>
</svg>

<div class="ph" role="img" aria-label="Bouquet of pink gerbera daisies with green palm leaves" style="left:540px;top:120px;width:660px;height:480px;background:radial-gradient(ellipse at 55% 60%,#f0758a 0%,#f59aa8 35%,#f7d0d6 65%,rgba(251,230,236,0) 80%)"></div>
<div class="abs hero-title">GORGEOUS FLOWERS FOR YOUR</div>
<div class="abs script hero-script">Special Events</div>
<div class="btn" style="left:120px;top:440px;width:130px;height:40px">Shop now</div>
<div class="dots" style="left:582px;top:636px"><i class="on"></i><i></i><i></i></div>

<div class="ph" role="img" aria-label="Pink rose watercolour bloom" style="left:190px;top:660px;width:130px;height:100px;border-radius:50%;background:radial-gradient(circle,#f6c3cc,rgba(246,195,204,0) 70%)"></div>
<div class="ph" role="img" aria-label="Pink rose with leaves" style="left:0;top:900px;width:120px;height:160px;border-radius:50%;background:radial-gradient(circle,#f4bfc8,rgba(244,191,200,0) 70%)"></div>
<div class="ph" role="img" aria-label="Florist shop shelves with colourful bouquets" style="left:120px;top:780px;width:260px;height:420px;background:linear-gradient(160deg,#b7a8c6,#e8c6d4 45%,#8a9a74 100%)"></div>
<div class="ph" role="img" aria-label="Pink and white rose arrangement" style="left:380px;top:1110px;width:210px;height:230px;border:4px solid #fff;background:linear-gradient(150deg,#d9899a,#f1d3dc 50%,#8c9c6e)"></div>
<div class="abs script welcome-bg">Welcome</div>
<div class="abs welcome-title">Exclusive Design by<br>Best Florists</div>
<p class="abs body-text" style="left:595px;top:960px;width:380px">Lorem Ipsum is simply dummy text of the printing and typesetting industry. Lorem Ipsum has been the industry's standard dummy text ever since the 1500s.</p>
<div class="btn" style="left:595px;top:1035px;width:130px;height:40px">Shop now</div>
<div class="ph" role="img" aria-label="Pink rose with leaves" style="left:1040px;top:1180px;width:160px;height:200px;border-radius:50%;background:radial-gradient(circle,#f4c3cb,rgba(244,195,203,0) 70%)"></div>

<div class="abs kicker" style="left:0;top:1445px;width:1200px">Wounderful Flowers</div>
<div class="abs script script-head" style="left:0;top:1490px;width:1200px">Feature Products</div>
<svg class="abs arrow" style="left:55px" viewBox="0 0 20 20" fill="none" stroke="#2a2226" stroke-width="2"><path d="M13 3l-7 7 7 7"/></svg>
<svg class="abs arrow" style="left:1125px" viewBox="0 0 20 20" fill="none" stroke="#2a2226" stroke-width="2"><path d="M7 3l7 7-7 7"/></svg>

<div class="product" style="left:105px">
  <div class="pic" role="img" aria-label="Red rose bouquet in white wrap" style="background:linear-gradient(180deg,#c8223a 0%,#e45a66 45%,#f3eaea 60%,#e9e1e1)"></div>
  <div class="name">Name of product # 01</div><div class="price">$40</div>
</div>
<div class="product active" style="left:350px">
  <div class="pic" role="img" aria-label="Pink mixed bouquet in pink paper" style="background:linear-gradient(180deg,#e79bb0,#f2b8c7 45%,#f6a9bd)"></div>
  <div class="name">Name of product # 01</div><div class="price">$40</div>
  <div class="btn" style="left:55px;top:355px;width:90px;height:28px;font-size:11px;text-transform:none;background:var(--rose);color:#fff">Add to Cart</div>
</div>
<div class="product" style="left:640px">
  <div class="pic" role="img" aria-label="Red tulip bouquet" style="background:linear-gradient(180deg,#c9243c 0%,#db5a66 35%,#7c9a5c 60%,#6f8c54)"></div>
  <div class="name">Name of product # 01</div><div class="price">$40</div>
</div>
<div class="product" style="left:880px">
  <div class="pic" role="img" aria-label="White calla lily bouquet" style="background:linear-gradient(180deg,#f4f1ea 0%,#e8e4da 40%,#8fa56f 70%,#7b9660)"></div>
  <div class="name">Name of product # 01</div><div class="price">$40</div>
</div>
<div class="btn" style="left:510px;top:2120px;width:180px;height:40px">Browse more</div>
<div class="ph" role="img" aria-label="Pink roses with leaves" style="left:0;top:2020px;width:200px;height:260px;border-radius:50%;background:radial-gradient(circle,#f4c1ca,rgba(244,193,202,0) 70%)"></div>
<div class="ph" role="img" aria-label="Green leaf sprigs" style="left:960px;top:2080px;width:240px;height:240px;border-radius:50%;background:radial-gradient(circle,#d8dcc0,rgba(216,220,192,0) 70%)"></div>

<div class="abs kicker" style="left:0;top:2275px;width:1200px">Reviews</div>
<div class="abs script script-head" style="left:0;top:2315px;width:1200px">Testimonials</div>
<div class="abs" style="left:175px;top:2420px;font-size:40px;font-weight:600;line-height:1">“</div>
<p class="abs body-text" style="left:210px;top:2435px;width:780px;text-align:center;color:var(--ink)">Lorem Ipsum is simply dummy text of the printing and typesetting industry. Lorem Ipsum has been the industry's standard dummy text ever since the 1500s, when an unknown printer took a galley of type and scrambled it to make a type specimen book. It has survived not only five centuries but also the leap into electronic typesetting, remaining essentially unchanged.</p>
<div class="abs" style="left:1000px;top:2500px;font-size:40px;font-weight:600;line-height:1">”</div>
<div class="abs script" style="left:0;top:2520px;width:1200px;text-align:center;font-size:26px">Maria</div>
<div class="dots" style="left:582px;top:2598px"><i class="on"></i><i></i><i></i></div>

<div class="abs" style="left:120px;top:2635px;font-size:20px;font-weight:500">Latest Articles</div>
<div class="abs script" style="left:120px;top:2672px;font-size:52px;line-height:1.1">Blog Posts</div>
<div class="btn" style="left:925px;top:2690px;width:150px;height:40px">Browse more</div>
<div class="post" style="left:120px">
  <div class="pic" role="img" aria-label="Pink blossom branch" style="background:linear-gradient(135deg,#e7a6b8,#cf6f8a 50%,#f1dbe2)"></div>
  <div class="date">June<br>12</div>
  <h4>Article title # 01</h4>
  <p>Lorem Ipsum is simply dummy text of the printing and typesetting industry. Lorem Ipsum has been the industry's standard dummy text ever.</p>
</div>
<div class="post" style="left:450px">
  <div class="pic" role="img" aria-label="Purple and magenta chrysanthemums" style="background:linear-gradient(135deg,#a23c9c,#d76fbf 50%,#7b2a7c)"></div>
  <div class="date">June<br>12</div>
  <h4>Article title # 02</h4>
  <p>Lorem Ipsum is simply dummy text of the printing and typesetting industry. Lorem Ipsum has been the industry's standard dummy text ever.</p>
</div>
<div class="post" style="left:780px">
  <div class="pic" role="img" aria-label="Orange and yellow chrysanthemums" style="background:linear-gradient(135deg,#e3892e,#f2b642 50%,#c9502e)"></div>
  <div class="date">June<br>12</div>
  <h4>Article title # 03</h4>
  <p>Lorem Ipsum is simply dummy text of the printing and typesetting industry. Lorem Ipsum has been the industry's standard dummy text ever.</p>
</div>
<div class="ph" role="img" aria-label="Green leaf sprigs" style="left:0;top:3100px;width:180px;height:130px;border-radius:50%;background:radial-gradient(circle,#d9dcc2,rgba(217,220,194,0) 70%)"></div>
<div class="ph" role="img" aria-label="Pink rose" style="left:1020px;top:3080px;width:180px;height:150px;border-radius:50%;background:radial-gradient(circle,#f4c2cb,rgba(244,194,203,0) 70%)"></div>

<div class="abs band"></div>
<div class="abs" style="left:120px;top:3262px;font-size:26px;font-weight:500;color:#fff">Join us for our latest news updates</div>
<p class="abs" style="left:120px;top:3305px;width:420px;font-size:13px;line-height:1.5;color:#fbe3e7">Lorem Ipsum is simply dummy text of the printing and typesetting industry. Lorem Ipsum has been the industry's standard dummy text ever since the 1500s.</p>
<div class="abs" style="left:645px;top:3310px;width:430px;height:40px;border:1px solid #fff;border-radius:22px;padding:11px 18px;font-size:12px;color:#fbe3e7">Enter email</div>
<div class="btn" style="left:955px;top:3312px;width:118px;height:36px;background:#fff;font-size:13px">Subscribe</div>

<div class="abs footer"></div>
<div class="logo" style="top:3500px;font-size:24px;left:480px;width:240px">Petal &amp; Fern</div>
<div class="col-h" style="left:120px">Contact info.</div>
<div class="col-h" style="left:385px">Quick links</div>
<div class="col-h" style="left:585px">Account</div>
<div class="col-h" style="left:790px">Follow us</div>
<svg class="abs" style="left:120px;top:3692px" width="16" height="140" viewBox="0 0 16 140" fill="#2a2226">
  <path d="M8 1a5 5 0 0 0-5 5c0 4 5 10 5 10s5-6 5-10a5 5 0 0 0-5-5zm0 7a2 2 0 1 1 0-4 2 2 0 0 1 0 4z"/>
  <path d="M3 50l3-2 3 4-2 2c1 2 3 4 5 5l2-2 4 3-2 3c-6 0-13-7-13-13z"/>
  <rect x="1" y="92" width="14" height="10" rx="1" fill="none" stroke="#2a2226" stroke-width="1.5"/><path d="M1 93l7 5 7-5" fill="none" stroke="#2a2226" stroke-width="1.5"/>
</svg>
<div class="abs" style="left:145px;top:3690px;font-size:13px;line-height:1.5">412 Birchwood Lane,<br>Maple Hollow, CA 90001</div>
<div class="abs" style="left:145px;top:3738px;font-size:13px">1-555-010-2040</div>
<div class="abs" style="left:145px;top:3782px;font-size:13px">hello@petalfern.com</div>
<div class="abs" style="left:120px;top:3852px;display:flex;gap:14px">
  <span style="width:16px;height:16px;border-radius:50%;background:var(--ink)"></span>
  <span style="width:16px;height:16px;border-radius:50%;background:var(--ink)"></span>
  <span style="width:16px;height:16px;border-radius:50%;background:var(--ink)"></span>
  <span style="width:16px;height:16px;border-radius:50%;background:var(--ink)"></span>
  <span style="width:16px;height:16px;border-radius:50%;background:var(--ink)"></span>
</div>
<div class="links" style="left:385px">Shop<br>About<br>Blog<br>Contact<br>Arrangement<br>Bouquets<br>Everlasting arrangements<br>Gifts</div>
<div class="links" style="left:585px">Login<br>Signup<br>My Profile<br>My cart<br>Checkout<br>Return Policy</div>
<div class="ph" role="img" aria-label="White rose arrangement" style="left:790px;top:3690px;width:88px;height:88px;background:linear-gradient(135deg,#eee8e6,#c7c0bf)"></div>
<div class="ph" role="img" aria-label="Purple bouquet" style="left:890px;top:3690px;width:88px;height:88px;background:linear-gradient(135deg,#8f77a9,#c9b5d6)"></div>
<div class="ph" role="img" aria-label="Blue hydrangeas" style="left:990px;top:3690px;width:88px;height:88px;background:linear-gradient(135deg,#7f95c4,#b6c3df)"></div>
<div class="ph" role="img" aria-label="Pink and green bouquet" style="left:790px;top:3790px;width:88px;height:88px;background:linear-gradient(135deg,#d98fa2,#8ba071)"></div>
<div class="ph" role="img" aria-label="Violet flowers" style="left:890px;top:3790px;width:88px;height:88px;background:linear-gradient(135deg,#6b3f86,#b37bb8)"></div>
<div class="ph" role="img" aria-label="Purple hydrangea" style="left:990px;top:3790px;width:88px;height:88px;background:linear-gradient(135deg,#8d6fb0,#d1bfe0)"></div>
<div class="abs" style="left:655px;top:3915px;display:flex;gap:10px">
  <span style="width:36px;height:22px;border-radius:3px;background:#e7dcd8"></span>
  <span style="width:36px;height:22px;border-radius:3px;background:#e7dcd8"></span>
  <span style="width:36px;height:22px;border-radius:3px;background:#e7dcd8"></span>
  <span style="width:36px;height:22px;border-radius:3px;background:#e7dcd8"></span>
</div>
<div class="abs copyright">Copyright © 2023 Petal &amp; Fern &nbsp;|&nbsp; Privacy Policy</div>
</body>
</html>
```